Dance Studio Launch Poster

We are looking for an A2 size poster to advertise our new dance studios. The new studios open on the 1st of November and we will be offering a 50% discount off the 2015 Term 1 fees for anyone who joins us between now and the end of the year. The poster will be located inside a lift/elevator within the building where our studios are located.

Our programme include dance classes from ages 2+. The majority of our business comes from our graded ballet or tap classes, so this should be the main focus. However we also have pre-school classes as well as an adults programme.

Our website is currently being upgraded but you can find more information at both www.brightlanedancehall.com.sg and www.facebook.com/BrightLaneDanceHallSG

I have attached some photos and existing flyers for reference.

If you have any questions or need any additional photos or information, please message me.

Target Market(s)

Parents on children aged 2 to 16

Industry/Entity Type

Dance Studio

Requirements
Must have
• Logo, address, special offer

```html
<!DOCTYPE html>
<html lang="en">
<head>
<meta charset="utf-8">
<title>Bright Lane Dance Hall – Term 1 Offer</title>
<link rel="stylesheet" href="https://fonts.googleapis.com/css2?family=Jost:wght@500;600;800&family=Barlow:wght@400;500&display=swap">
<style>
  :root {
    --paper: #ffffff;
    --brand-blue: #1f6fb4;
    --banner-blue: #1a64ab;
    --offer-orange: #f07021;
    --ink: #2a2a2a;
    --muted: #8a8a8a;
    --rule: #6f6f6f;
    --band-1: #2f78bf;
    --band-2: #6aa3d8;
    --band-3: #b9d4ee;
  }
  * { margin: 0; padding: 0; box-sizing: border-box; }
  html, body { width: 850px; height: 1200px; overflow: hidden; background: var(--paper); }
  .poster {
    position: relative; width: 850px; height: 1200px; overflow: hidden;
    background: var(--paper); font-family: "Jost", "Helvetica Neue", Arial, sans-serif; color: var(--ink);
  }
  .collage { position: absolute; inset: 0; }

  .brand {
    position: absolute; left: 32px; top: 92px; width: 330px;
    display: flex; align-items: center; gap: 14px;
  }
  .brand-dot { width: 24px; height: 24px; border-radius: 50%; background: var(--brand-blue); flex: none; }
  .brand-name {
    font-weight: 600; font-size: 44px; line-height: 1.02;
    color: var(--brand-blue); letter-spacing: -0.5px;
  }

  .offer-tag { position: absolute; left: 36px; top: 296px; width: 362px; height: 196px; }
  .offer-text { position: absolute; left: 36px; top: 296px; width: 340px; height: 196px; color: #fff; font-weight: 800; line-height: 1; }
  .offer-percent { position: absolute; left: 30px; top: 22px; font-size: 100px; letter-spacing: -3px; }
  .offer-word { position: absolute; left: 30px; top: 124px; font-size: 54px; letter-spacing: 0; }
  .offer-note {
    position: absolute; left: 38px; top: 494px; font-family: "Barlow", sans-serif; font-weight: 500;
    font-size: 20.5px; letter-spacing: 0.9px; color: var(--ink); white-space: nowrap;
  }
  .opening {
    position: absolute; left: 38px; top: 524px; font-family: "Barlow", sans-serif; font-weight: 400;
    font-size: 14.5px; line-height: 1.35; letter-spacing: 0.4px; color: var(--muted);
  }
  .opening strong { color: var(--brand-blue); font-weight: 500; }

  .classes { position: absolute; left: 0; top: 592px; width: 360px; height: 470px; list-style: none; }
  .class-label { position: absolute; left: 22px; color: #fff; font-weight: 800; font-size: 32px; line-height: 66px; letter-spacing: 0.5px; }

  .contact { position: absolute; left: 80px; top: 1108px; width: 330px; font-family: "Barlow", sans-serif; font-weight: 400; font-size: 17px; color: var(--muted); }
  .contact-row { position: absolute; display: flex; align-items: center; gap: 7px; white-space: nowrap; }
  .contact-row svg { flex: none; }
  .contact-phone { font-size: 19px; }
</style>
</head>
<body>
<main class="poster">

  <svg class="collage" width="850" height="1200" viewBox="0 0 850 1200">
    <defs>
      <linearGradient id="wedge" x1="0" y1="0" x2="1" y2="1">
        <stop offset="0" stop-color="#1a64ab" stop-opacity="0"/>
        <stop offset="1" stop-color="#1a64ab"/>
      </linearGradient>
      <linearGradient id="tile-floor-class" x1="0" y1="0" x2="1" y2="1">
        <stop offset="0" stop-color="#b48a62"/><stop offset="0.5" stop-color="#e8ddd0"/><stop offset="1" stop-color="#5a4636"/>
      </linearGradient>
      <linearGradient id="tile-barre" x1="0" y1="0" x2="1" y2="1">
        <stop offset="0" stop-color="#b99a78"/><stop offset="0.45" stop-color="#3f67c4"/><stop offset="1" stop-color="#203f8f"/>
      </linearGradient>
      <linearGradient id="tile-tutu" x1="0" y1="0" x2="1" y2="1">
        <stop offset="0" stop-color="#8a6a4a"/><stop offset="0.5" stop-color="#e6cdb4"/><stop offset="1" stop-color="#d9d3cc"/>
      </linearGradient>
      <linearGradient id="tile-stretch" x1="0" y1="0" x2="0" y2="1">
        <stop offset="0" stop-color="#c4c2c0"/><stop offset="0.5" stop-color="#3c63bd"/><stop offset="1" stop-color="#2c2c34"/>
      </linearGradient>
      <linearGradient id="tile-tap" x1="0" y1="0" x2="1" y2="1">
        <stop offset="0" stop-color="#3a3a3a"/><stop offset="0.5" stop-color="#d4d4d4"/><stop offset="1" stop-color="#5a5a5a"/>
      </linearGradient>
      <linearGradient id="tile-boy" x1="0" y1="0" x2="1" y2="1">
        <stop offset="0" stop-color="#7a5a38"/><stop offset="0.55" stop-color="#efe8df"/><stop offset="1" stop-color="#3a2c22"/>
      </linearGradient>
      <linearGradient id="tile-lesson" x1="0" y1="0" x2="1" y2="1">
        <stop offset="0" stop-color="#c08a3a"/><stop offset="0.5" stop-color="#4a4fa8"/><stop offset="1" stop-color="#1c1c22"/>
      </linearGradient>
      <linearGradient id="band-fade" x1="0" y1="0" x2="1" y2="0">
        <stop offset="0" stop-color="#7a7a7a" stop-opacity="0.9"/><stop offset="1" stop-color="#7a7a7a" stop-opacity="0"/>
      </linearGradient>
    </defs>

    <g class="photo-tiles">
      <polygon points="492,0 850,0 850,138 724,236" fill="url(#tile-floor-class)" role="img" aria-label="Photo: young children sitting on the studio floor with their teacher"/>
      <polygon points="330,228 484,20 712,256 558,442" fill="url(#tile-barre)" role="img" aria-label="Photo: ballet students in blue leotards and hair ribbons at the barre"/>
      <polygon points="686,330 850,150 850,478" fill="url(#tile-tutu)" role="img" aria-label="Photo: little girl in a white tutu sitting on the floor"/>
      <polygon points="518,490 690,342 850,498 850,662 758,716" fill="url(#tile-stretch)" role="img" aria-label="Photo: young ballet student in a blue leotard stretching on the studio floor"/>
      <polygon points="355,700 520,536 742,746 592,906" fill="url(#tile-tap)" role="img" aria-label="Black and white photo: two boys putting on tap shoes"/>
      <polygon points="664,832 846,682 850,686 850,1016" fill="url(#tile-boy)" role="img" aria-label="Photo: young boy in a white T-shirt during a dance class"/>
      <polygon points="500,1072 682,880 850,1034 850,1200 622,1200" fill="url(#tile-lesson)" role="img" aria-label="Photo: teacher guiding a young dancer's arm position"/>
    </g>

    <polygon points="404,318 570,468 540,476" fill="url(#wedge)"/>
    <polygon points="368,716 588,938 556,950" fill="url(#wedge)"/>

    <g class="class-banners">
      <g transform="translate(0,593)">
        <rect x="0" y="70" width="250" height="5" fill="url(#band-fade)"/>
        <polygon points="0,0 278,0 308,33 278,66 0,66" fill="var(--banner-blue)"/>
        <line x1="272" y1="-4" x2="345" y2="80" stroke="var(--rule)" stroke-width="1.5"/>
        <line x1="272" y1="70" x2="345" y2="-14" stroke="var(--rule)" stroke-width="1.5"/>
      </g>
      <g transform="translate(0,723)">
        <rect x="0" y="70" width="250" height="5" fill="url(#band-fade)"/>
        <polygon points="0,0 278,0 308,33 278,66 0,66" fill="var(--banner-blue)"/>
        <line x1="272" y1="-4" x2="345" y2="80" stroke="var(--rule)" stroke-width="1.5"/>
        <line x1="272" y1="70" x2="345" y2="-14" stroke="var(--rule)" stroke-width="1.5"/>
      </g>
      <g transform="translate(0,853)">
        <rect x="0" y="70" width="250" height="5" fill="url(#band-fade)"/>
        <polygon points="0,0 278,0 308,33 278,66 0,66" fill="var(--banner-blue)"/>
        <line x1="272" y1="-4" x2="345" y2="80" stroke="var(--rule)" stroke-width="1.5"/>
        <line x1="272" y1="70" x2="345" y2="-14" stroke="var(--rule)" stroke-width="1.5"/>
      </g>
      <g transform="translate(0,983)">
        <rect x="0" y="70" width="250" height="5" fill="url(#band-fade)"/>
        <polygon points="0,0 278,0 308,33 278,66 0,66" fill="var(--banner-blue)"/>
        <line x1="272" y1="-4" x2="345" y2="80" stroke="var(--rule)" stroke-width="1.5"/>
        <line x1="272" y1="70" x2="345" y2="-14" stroke="var(--rule)" stroke-width="1.5"/>
      </g>
    </g>

    <polygon points="0,1110 30,1110 130,1200 0,1200" fill="var(--band-1)"/>
    <polygon points="0,1150 150,1150 200,1200 0,1200" fill="var(--band-2)" opacity="0.85"/>
    <polygon points="0,1180 280,1180 300,1200 0,1200" fill="var(--band-3)"/>
  </svg>

  <header class="brand">
    <span class="brand-dot"></span>
    <span class="brand-name">Bright Lane<br>Dance Hall</span>
  </header>

  <svg class="offer-tag" width="362" height="196" viewBox="0 0 362 196">
    <path d="M12,4 H270 L356,84 V184 Q356,192 348,192 H12 Q4,192 4,184 V12 Q4,4 12,4 Z" fill="var(--offer-orange)"/>
    <path d="M20,14 H266 L346,88 V174 Q346,182 338,182 H20 Q14,182 14,176 V20 Q14,14 20,14 Z" fill="none" stroke="#fff" stroke-width="3"/>
  </svg>
  <div class="offer-text">
    <span class="offer-percent">50%</span>
    <span class="offer-word">DISCOUNT</span>
  </div>
  <p class="offer-note">off the 2015 Term 1 fees for anyone</p>
  <p class="opening"><strong>New studios open 1 November</strong><br>18 Lane Road, #03-05, Singapore 238870</p>

  <ul class="classes">
    <li class="class-label" style="top:1px">MELODY CUB</li>
    <li class="class-label" style="top:131px">TAP</li>
    <li class="class-label" style="top:261px">BALLET</li>
    <li class="class-label" style="top:391px">LITTLE STARS</li>
  </ul>

  <footer class="contact">
    <div class="contact-row" style="left:5px; top:2px">
      <svg width="18" height="18" viewBox="0 0 18 18"><circle cx="9" cy="9" r="7.5" fill="none" stroke="var(--brand-blue)" stroke-width="1.6"/><ellipse cx="9" cy="9" rx="3.2" ry="7.5" fill="none" stroke="var(--brand-blue)" stroke-width="1.4"/><line x1="1.5" y1="9" x2="16.5" y2="9" stroke="var(--brand-blue)" stroke-width="1.4"/></svg>
      <span>www.brightlanedancehall.com.sg</span>
    </div>
    <div class="contact-row" style="left:90px; top:30px">
      <svg width="18" height="13" viewBox="0 0 18 13"><rect x="1" y="1" width="16" height="11" fill="none" stroke="var(--brand-blue)" stroke-width="1.6"/><polyline points="1,1 9,8 17,1" fill="none" stroke="var(--brand-blue)" stroke-width="1.6"/></svg>
      <span>hello@brightlanedance.com.sg</span>
    </div>
    <div class="contact-row contact-phone" style="left:185px; top:55px">
      <svg width="22" height="22" viewBox="0 0 22 22"><circle cx="11" cy="11" r="10" fill="none" stroke="var(--brand-blue)" stroke-width="1.6"/><path d="M7.5 6c.8-.5 1.4-.3 1.8.4l.8 1.6c.3.6.1 1.1-.4 1.5l-.6.4c.6 1.4 1.5 2.4 2.9 3l.4-.6c.4-.5 1-.7 1.5-.4l1.6.8c.7.4.9 1 .4 1.8-.7 1-1.8 1.4-3 1-2.8-1-4.8-3-5.8-5.8-.4-1.2 0-2.3 1-3z" fill="var(--brand-blue)"/></svg>
      <span>8240 5716</span>
    </div>
  </footer>

</main>
</body>
</html>
```